BOLD & MINIMALIST DESIGN NEEDED

We want a very bold but minimalistic business card design that is impactful and utilizes both sides of the business card. Our current logo is included for your use.

We want bold fonts and good use of negative space. We don't want the logo to overpower the design.

Target Market(s)

Professionals who are building new commercial buildings.

Industry/Entity Type

Construction

Contact Information for Business Card

Name, Title, email, office phone, cell phone, website

Font styles to use
Serif
Sans Serif

Requirements
Must have
• Bold design!

```html
<!DOCTYPE html>
<html lang="en">
<head>
<meta charset="utf-8">
<title>Ridgeline Build Co — Business Card</title>
<link href="https://fonts.googleapis.com/css2?family=Montserrat:wght@400;600;700&display=swap" rel="stylesheet">
<style>
  :root {
    --backdrop: #dcdcdc;
    --ink: #0d0e10;
    --paper: #ffffff;
    --green: #8fcf55;
    --grey-text: #6f6f6f;
  }
  * { margin: 0; padding: 0; box-sizing: border-box; }
  html, body {
    width: 1200px; height: 1200px; overflow: hidden;
    background: var(--backdrop);
    font-family: "Montserrat", Arial, sans-serif;
  }
  .card {
    position: absolute; left: 180px; width: 867px; height: 499px;
    background: var(--ink); overflow: hidden;
  }
  .card--front { top: 85px; }
  .card--back { top: 626px; }

  .brand {
    position: absolute; display: flex; align-items: center; gap: 14px;
    font-weight: 700; letter-spacing: 1px; white-space: nowrap;
  }
  .brand__mark { width: 22px; height: 22px; background: var(--green); }
  .brand--front {
    left: 50%; top: 50%; transform: translate(-50%, -50%);
    color: var(--paper); font-size: 42px;
  }
  .brand--back {
    left: 183px; top: 250px; transform: translate(-50%, -50%);
    color: var(--ink); font-size: 34px;
  }

  .back-shape { position: absolute; inset: 0; width: 867px; height: 499px; }

  .person { position: absolute; right: 40px; top: 113px; text-align: right; }
  .person__name { color: var(--paper); font-weight: 700; font-size: 30px; letter-spacing: 0.5px; line-height: 38px; }
  .person__title { color: var(--green); font-weight: 400; font-size: 25px; letter-spacing: 1px; line-height: 30px; }

  .contact {
    position: absolute; display: flex; flex-direction: column; gap: 9px;
    color: var(--grey-text); font-size: 23px; letter-spacing: 1.5px;
  }
  .contact--phones { left: 32px; top: 409px; }
  .contact--web { left: 444px; top: 408px; }
  .contact__row { display: flex; align-items: center; gap: 12px; height: 26px; }
  .contact__icon { width: 24px; height: 24px; flex: none; }
  .contact__accent { color: var(--green); }
</style>
</head>
<body>

<section class="card card--front" aria-label="Card front">
  <div class="brand brand--front">
    <span class="brand__mark"></span>
    <span class="brand__name">RIDGELINE BUILD CO</span>
  </div>
</section>

<section class="card card--back" aria-label="Card back">
  <svg class="back-shape" viewBox="0 0 867 499" aria-hidden="true">
    <polygon points="0,185 185,99 867,446 867,499 0,499" fill="var(--paper)"/>
    <polygon points="0,177 185,72 792,409 185,99 0,185" fill="var(--green)"/>
  </svg>

  <div class="brand brand--back">
    <span class="brand__mark"></span>
    <span class="brand__name">RIDGELINE</span>
  </div>

  <div class="person">
    <p class="person__name">Name Surename</p>
    <p class="person__title">Director</p>
  </div>

  <div class="contact contact--phones">
    <div class="contact__row">
      <svg class="contact__icon" viewBox="0 0 24 24" aria-hidden="true">
        <path d="M5 3l4 1 1 5-2.5 1.5a12 12 0 0 0 6 6L15 14l5 1 1 4-2 2C10 21 3 14 3 5z" fill="var(--ink)"/>
      </svg>
      <span>555-014-2200</span>
    </div>
    <div class="contact__row">
      <svg class="contact__icon" viewBox="0 0 24 24" aria-hidden="true">
        <path d="M2 9c0-4 20-4 20 0v2h-5V9H7v2H2z" fill="var(--ink)"/>
        <path d="M6 12h12l3 8H3z" fill="var(--ink)"/>
        <circle cx="12" cy="16" r="2" fill="var(--paper)"/>
      </svg>
      <span>555-014-2200</span>
    </div>
  </div>

  <div class="contact contact--web">
    <div class="contact__row">
      <svg class="contact__icon" viewBox="0 0 24 24" aria-hidden="true">
        <rect x="2" y="5" width="20" height="14" fill="var(--ink)"/>
        <polyline points="3,6 12,13 21,6" fill="none" stroke="var(--paper)" stroke-width="1.5"/>
      </svg>
      <span>info@rb-co.com</span>
    </div>
    <div class="contact__row">
      <svg class="contact__icon" viewBox="0 0 24 24" aria-hidden="true">
        <g fill="none" stroke="var(--ink)" stroke-width="1.6">
          <circle cx="12" cy="12" r="10"/>
          <ellipse cx="12" cy="12" rx="4.5" ry="10"/>
          <line x1="2" y1="12" x2="22" y2="12"/>
          <line x1="4" y1="7" x2="20" y2="7"/>
          <line x1="4" y1="17" x2="20" y2="17"/>
        </g>
      </svg>
      <span>www.<span class="contact__accent">rb-co</span>.com</span>
    </div>
  </div>
</section>

</body>
</html>
```